依頼詳細
1.渡航先の選択ページのデザイン
2.出発日の選択ページのデザイン
3.滞在期間の選択ページのデザイン
4.渡航目的の選択ページのデザイン
5.予約方法の選択ページのデザイン

流れが明確であれば、全て繋がった1ページ構成でも結構です

詳しくは添付資料を参照願います
ページ数
5ページ
希望イメージ
シンプル 複雑
単色 カラフル
暗い 明るい
日常 高級
遊び心 厳粛
未来的 伝統的
女性的 男性的
希望する色
青系、濃紺を主にした色合いでお願いいたします
納品ファイル
• 高解像度JPG (.jpg)
補足説明
スクリーンショットおよび、
サイトを構成するファイル一式をご納品いただきます
提案者制限を付加させいただきました
ファイル一式についての補足ですが、AIやPSD等の
画像を作成したツールでの保存形式ファイルもご納品のほどよろしくお願いいたします。
■ 選んだ理由

レベルの高いご提案を頂き、選定に悩みましたが、
「目指すコンセプトとの一致」と作り込み、質問を頂だいた事を鑑みて、選定とさせて頂きました。

■ 提案者全員のお礼・コメント

大変多くのご提案を頂き、どのデザインも甲乙付けがたいご提案で選定に悩みました。
今後また別の機会に、お力添えを頂ければ幸いです。
この度は誠にご提案ありがとうございました。

```html
<!DOCTYPE html>
<html lang="ja">
<head>
<meta charset="utf-8">
<title>新規予約</title>
<link href="https://fonts.googleapis.com/css2?family=Noto+Sans+JP:wght@400;500;700&display=swap" rel="stylesheet">
<style>
  :root {
    --navy: #35478c;
    --navy-dark: #2d3d7a;
    --ink: #333a4d;
    --muted: #555b6b;
    --cyan: #1ea5e3;
    --highlight: #dbe8f6;
    --line: #b9bfcc;
    --white: #ffffff;
  }
  * { box-sizing: border-box; margin: 0; padding: 0; }
  html, body { width: 1200px; height: 2596px; overflow: hidden; background: var(--white); }
  body { font-family: "Noto Sans JP", sans-serif; color: var(--ink); position: relative; }

  .app-header {
    position: absolute; left: 0; top: 0; width: 1200px; height: 140px;
    background: var(--navy); color: var(--white);
    display: flex; align-items: center; justify-content: center;
  }
  .app-header__title { font-size: 52px; font-weight: 700; letter-spacing: 2px; }
  .app-header__menu { position: absolute; right: 40px; top: 46px; }

  .section-title {
    position: absolute; left: 80px; font-size: 48px; font-weight: 700; color: var(--navy);
    line-height: 1; padding: 0 4px 6px;
    background: linear-gradient(transparent 55%, var(--highlight) 55%);
  }

  .select-button {
    position: absolute; top: 368px; height: 128px;
    border: 3px solid var(--navy); background: var(--white);
    display: flex; align-items: center; justify-content: center;
    font-size: 44px; color: var(--ink);
  }

  .tag {
    position: absolute; height: 68px; background: var(--cyan); color: var(--white);
    font-size: 42px; font-weight: 500; display: flex; align-items: center;
    padding: 0 12px; gap: 10px; border-radius: 4px; letter-spacing: 2px;
  }
  .tag__close { font-size: 44px; font-weight: 700; }

  .date-select {
    position: absolute; top: 932px; height: 128px;
    border: 3px solid #d3d6de; border-radius: 8px; background: var(--white);
    font-size: 44px; display: flex; align-items: center; padding-left: 36px;
  }
  .date-select::after {
    content: ""; position: absolute; right: 32px; top: 54px;
    border-left: 12px solid transparent; border-right: 12px solid transparent;
    border-top: 14px solid #888;
  }
  .date-unit { position: absolute; top: 960px; font-size: 48px; }

  .radio {
    position: absolute; display: flex; align-items: center; gap: 28px;
    font-size: 44px; color: var(--ink);
  }
  .radio__mark {
    width: 46px; height: 46px; border-radius: 50%; border: 3px solid #9aa0ad;
    flex: none; position: relative; background: var(--white);
  }
  .radio--checked .radio__mark { border-color: var(--cyan); }
  .radio--checked .radio__mark::after {
    content: ""; position: absolute; inset: 8px; border-radius: 50%; background: var(--cyan);
  }
  .radio__note { position: absolute; left: 226px; font-size: 28px; color: var(--muted); }

  .submit-button {
    position: absolute; left: 48px; top: 2392px; width: 1104px; height: 152px;
    background: var(--navy); color: var(--white); font-size: 52px; font-weight: 700;
    display: flex; align-items: center; justify-content: center; letter-spacing: 2px;
  }
</style>
</head>
<body>
  <header class="app-header">
    <h1 class="app-header__title">新規予約</h1>
    <svg class="app-header__menu" width="88" height="48" viewBox="0 0 88 48" aria-label="メニュー">
      <rect x="0" y="0" width="88" height="5" fill="#fff"/>
      <rect x="20" y="21" width="68" height="5" fill="#fff"/>
      <rect x="40" y="42" width="48" height="5" fill="#fff"/>
    </svg>
  </header>

  <h2 class="section-title" style="top:250px">渡航先を選択してください（複数指定可能）</h2>
  <div class="select-button" style="left:128px;width:392px">地図から選択</div>
  <div class="select-button" style="left:560px;width:512px">キーワードから選択</div>
  <div class="tag" style="left:128px;top:548px">フランス<span class="tag__close">×</span></div>
  <div class="tag" style="left:416px;top:548px">イギリス<span class="tag__close">×</span></div>
  <div class="tag" style="left:712px;top:548px">ポルトガル<span class="tag__close">×</span></div>
  <div class="tag" style="left:128px;top:640px">フィンランド<span class="tag__close">×</span></div>

  <h2 class="section-title" style="top:826px">出発日を選択してください</h2>
  <div class="date-select" style="left:128px;width:240px">2021</div>
  <span class="date-unit" style="left:400px">年</span>
  <div class="date-select" style="left:484px;width:188px">05</div>
  <span class="date-unit" style="left:704px">月</span>
  <div class="date-select" style="left:792px;width:188px">23</div>
  <span class="date-unit" style="left:1012px">日</span>

  <h2 class="section-title" style="top:1188px">滞在期間を選択してください</h2>
  <label class="radio radio--checked" style="left:130px;top:1318px"><span class="radio__mark"></span>1ヶ月未満</label>
  <label class="radio" style="left:570px;top:1318px"><span class="radio__mark"></span>1ヶ月以上</label>

  <h2 class="section-title" style="top:1504px">渡航目的を選択してください</h2>
  <label class="radio radio--checked" style="left:130px;top:1618px"><span class="radio__mark"></span>仕事</label>
  <label class="radio" style="left:538px;top:1618px"><span class="radio__mark"></span>留学</label>
  <label class="radio" style="left:130px;top:1718px"><span class="radio__mark"></span>旅行</label>
  <label class="radio" style="left:538px;top:1718px"><span class="radio__mark"></span>その他</label>

  <h2 class="section-title" style="top:1904px">予約の種類を選択してください</h2>
  <label class="radio radio--checked" style="left:130px;top:2034px"><span class="radio__mark"></span>簡易予約</label>
  <p class="radio__note" style="top:2100px">簡単情報を入力するだけで来院予約ができます</p>
  <label class="radio" style="left:130px;top:2166px"><span class="radio__mark"></span>詳細予約</label>
  <p class="radio__note" style="top:2232px">詳細な情報を登録することで次回予約時の手間が省けます</p>

  <div class="submit-button">予約する</div>
</body>
</html>
```